New Podcast focussing on non-mainstream interventions for guidance needs podcast art

I need an exquisite piece of podcast art work for the launch of my new podcast 'Beyond the Still'. This podcast explores unorthodox, esoteric and unconventional methods to find peace, clarity and direction in life. Topics include family Constellations Systems, Psychedelics, Equine Therapy and Floatation to name a few. A teaser has been posted on Talvora with a strong response. The audience is primarily midlifers or those in a career/personal crisis of direction. It's meant to comfort, inform and empower and offer other ways rather than mainstream to work out what to do with your life. The file shared with you shows the pic used on Talvora as it's illustrating the idea of illumination. You can use it or not, and whilst I am ex-Military, I don't want the cover to convey an overly military influence. I'd like 'Beyond the Still' to feature on the art work and my name, Mirela Dunford. I'd like inspiration, creativity, and the idea of hope conveyed as well as clarity and courage. Whilst the podcast is about finding your direction please do no use compass images or cross road images as that is too obvious.
Hope that all helps. Looking forward to your ideas.

```html
<!DOCTYPE html>
<html lang="en">
<head>
<meta charset="utf-8">
<title>Beyond the Still — Mirela Dunford</title>
<link rel="stylesheet" href="https://fonts.googleapis.com/css2?family=Rubik+Dirt&family=Bebas+Neue&display=swap">
<style>
  :root {
    --night-olive: #141a09;
    --amber: #e0a82e;
    --khaki-light: #b39a6c;
    --khaki-mid: #6e6147;
    --khaki-dark: #524634;
    --sand: #a88b5c;
  }
  html, body {
    margin: 0;
    padding: 0;
    width: 1200px;
    height: 1200px;
    overflow: hidden;
    background: var(--night-olive);
  }
  .cover {
    position: relative;
    width: 1200px;
    height: 1200px;
    background: var(--night-olive);
  }
  .cover-art {
    position: absolute;
    inset: 0;
    width: 1200px;
    height: 1200px;
    display: block;
  }
  .title-word {
    font-family: "Rubik Dirt", "Impact", sans-serif;
    fill: url(#title-tone);
  }
  .title-link {
    font-family: "Rubik Dirt", "Impact", sans-serif;
    fill: var(--amber);
  }
  .host-name {
    font-family: "Bebas Neue", "Oswald", sans-serif;
    fill: var(--amber);
  }
</style>
</head>
<body>
<main class="cover">
  <svg class="cover-art" viewBox="0 0 1200 1200" xmlns="http://www.w3.org/2000/svg">
    <defs>
      <linearGradient id="title-tone" x1="0" y1="0" x2="1" y2="1">
        <stop offset="0" stop-color="var(--khaki-mid)"/>
        <stop offset="0.3" stop-color="var(--khaki-light)"/>
        <stop offset="0.55" stop-color="var(--khaki-dark)"/>
        <stop offset="0.8" stop-color="var(--khaki-light)"/>
        <stop offset="1" stop-color="var(--khaki-mid)"/>
      </linearGradient>
      <linearGradient id="figures-tone" x1="0" y1="0" x2="0" y2="1">
        <stop offset="0" stop-color="#141a09" stop-opacity="0"/>
        <stop offset="0.45" stop-color="#a88b5c" stop-opacity="0.55"/>
        <stop offset="1" stop-color="#a88b5c"/>
      </linearGradient>
    </defs>

    <rect class="backdrop" width="1200" height="1200" fill="var(--night-olive)"/>

    <rect class="figures-illustration" role="img"
          aria-label="Silhouettes of a group standing together on grassland at dusk"
          x="160" y="780" width="1040" height="420" fill="url(#figures-tone)"/>

    <text class="title-word title-top" x="118" y="364"
          font-size="300" textLength="950" lengthAdjust="spacingAndGlyphs">BEYOND</text>
    <text class="title-link" x="130" y="493"
          font-size="128" textLength="250" lengthAdjust="spacingAndGlyphs">THE</text>
    <text class="title-word title-bottom" x="126" y="788"
          font-size="300" textLength="648" lengthAdjust="spacingAndGlyphs">STILL</text>

    <text class="host-name host-first" x="821" y="572"
          font-size="64" letter-spacing="16">MIRELA</text>
    <text class="host-name host-last" x="821" y="633"
          font-size="64" letter-spacing="16">DUNFORD</text>
  </svg>
</main>
</body>
</html>
```